Designing a cover for my upcoming book.

A brief description of the theme which the book cover design has to capture is given below:
The title and sub-title of the book are as follows:
Title : Adrift Among Quiet Harbours
Sub-Title: Coastal Fisheries of the Lowlands - 3
The book is a critical examination of the laws which govern the conservation of wildlife in India. It describes how contradictory provisions within and between various laws make conservation of the same wildlife difficult which these laws are together meant to preserve. The book primarily discusses five laws which have a bearing on the subject, namely:
The Indian Forest Act, 1927;
The Wild Life (Protection) Act, 1972;
Forest (Conservation) Act, 1980
Biological Diversity Act, 2002; and
The Forest Rights Act, 2006.
Out of these five laws, the Wild Life (Protection) Act has been specifically mandated to protect wildlife. The primary objectives of other laws are different (as their names indicate) but all have a bearing on the conservation of wild animals as well. However all these laws have some contradictory provisions so that if the authorities comply with one law, they violate some other law. The same problem exists within the Wild Life (Protection) Act also. Many of its provisions can be enforced only by ignoring or violating others. As a result the authorities cannot devise a clear road map for conservation. Thus, conservation of wildlife in India is a victim of its own laws.
The book cover must illustrate this paradox. Perhaps the designer can create a tangle/web of these titles, running/cutting across each other, with one or more of charismatic Indian animals (e.g. tigers, elephants, leopards, spotted deer etc.) entangled in this mesh. The fonts and colours of the text (titles) can be artistically and creatively designed. If possible, the animal(s) should look a bit confused or perplexed. We can also show a ranger looking at this tangle in a helpless or confused manner (say raised hands thrown up).
This is only a suggestion. If the artist thinks he can depict the theme better in some other way, I will be happy to look at it.

Target Market(s)

Environmentalists, foresters, wildlife enthusiasts and conservationists, policy makers, advocates, environmental activists, lawyers, training institutes.

Requirements
Must have
• A beautiful picture of a tiger or some other Indian wild animal(s). Also, a net consisting of the names of the laws mentioned in the brief.
Nice to have
• The image of a ranger who looks a bit helpless and hassled. Perhaps in the background.

```html
<!DOCTYPE html>
<html lang="en">
<head>
<meta charset="utf-8">
<title>Adrift Among Quiet Harbours – Book Cover</title>
<link href="https://fonts.googleapis.com/css2?family=Cinzel:wght@400;600&family=Oswald:wght@400;500;600&display=swap" rel="stylesheet">
<style>
  :root {
    --backdrop: #2b2b2b;
    --paper: #f7f1ea;
    --title-brown: #7d4a3e;
    --title-dark: #3b3535;
    --subtitle-grey: #7a7777;
    --rule-grey: #5a5454;
    --fence-brown: #7a4638;
    --law-ink: #4e4340;
    --author-ink: #111111;
  }
  * { margin: 0; padding: 0; box-sizing: border-box; }
  html, body {
    width: 1200px; height: 1200px; overflow: hidden;
    background: var(--backdrop);
  }
  .cover {
    position: absolute; left: 223px; top: 36px;
    width: 754px; height: 1128px;
    background: var(--paper);
    overflow: hidden;
  }
  .title-line {
    position: absolute; left: 0; width: 100%;
    text-align: center; line-height: 1;
    font-family: "Oswald", "Arial Narrow", sans-serif;
    font-weight: 500; text-transform: uppercase;
    transform: translateY(-50%);
  }
  .title-top { top: 74px; font-size: 104px; color: var(--title-brown); }
  .title-bottom { top: 258px; font-size: 92px; color: var(--title-dark); }
  .title-joiner {
    top: 190px; font-size: 34px; color: var(--title-brown);
  }
  .joiner-rule {
    position: absolute; top: 189px; height: 2px;
    background: linear-gradient(90deg, transparent, var(--rule-grey) 30%, var(--rule-grey) 70%, transparent);
  }
  .joiner-rule.left { left: 119px; width: 204px; }
  .joiner-rule.right { left: 419px; width: 216px; }
  .subtitle {
    position: absolute; left: 0; top: 348px; width: 100%;
    text-align: center;
    font-family: "Cinzel", "Times New Roman", serif;
    font-weight: 400; font-size: 36px; line-height: 44px;
    color: var(--subtitle-grey);
  }
  .hero-art {
    position: absolute; left: 101px; top: 470px;
    width: 624px; height: 420px;
    border-radius: 46% 54% 40% 40% / 50% 50% 38% 38%;
    background:
      radial-gradient(ellipse at 20% 35%, #b7804c 0%, #9c6a3f 22%, transparent 45%),
      radial-gradient(ellipse at 65% 40%, #7d8660 0%, #9aa07e 35%, transparent 70%),
      radial-gradient(ellipse at 50% 80%, #c9b9a4 0%, transparent 70%);
    filter: blur(4px);
    opacity: 0.9;
  }
  .fence-art {
    position: absolute; left: 0; top: 742px;
    width: 100%; height: 273px;
    background: linear-gradient(180deg, rgba(160,100,80,0.18), rgba(160,100,80,0.10) 60%, rgba(160,100,80,0.16));
  }
  .fence-band {
    position: absolute; left: 0; width: 100%; height: 8px;
    background: var(--fence-brown);
  }
  .fence-band.top { top: 734px; }
  .fence-band.bottom { top: 1015px; }
  .law {
    position: absolute; white-space: nowrap; line-height: 1;
    font-family: "Oswald", "Arial Narrow", sans-serif;
    font-weight: 500; color: var(--law-ink);
    text-shadow: 0 0 2px var(--paper), 0 0 2px var(--paper);
  }
  .law-forest { left: 12px; top: 804px; font-size: 28px; }
  .law-rights { left: 418px; top: 864px; font-size: 26px; }
  .law-biodiversity { left: 409px; top: 934px; font-size: 17px; }
  .law-wildlife { left: 23px; top: 966px; font-size: 30px; }
  .law-conservation { left: 552px; top: 984px; font-size: 15px; }
  .author {
    position: absolute; left: 0; top: 1076px; width: 100%;
    transform: translateY(-50%);
    text-align: center; line-height: 1;
    font-family: "Cinzel", "Times New Roman", serif;
    font-weight: 600; font-size: 50px; color: var(--author-ink);
  }
</style>
</head>
<body>
  <main class="cover">
    <h1>
      <span class="title-line title-top">Adrift</span>
      <span class="joiner-rule left"></span>
      <span class="title-line title-joiner">Among</span>
      <span class="joiner-rule right"></span>
      <span class="title-line title-bottom">Quiet Harbours</span>
    </h1>
    <p class="subtitle">Coastal Fisheries of<br>the Lowlands - 3</p>

    <div class="hero-art" role="img" aria-label="Double-exposure image of a walking tiger whose body is filled with misty forest and a silhouetted ranger"></div>
    <div class="fence-art" role="img" aria-label="Brown chain-link fence mesh across the lower part of the cover"></div>
    <div class="fence-band top"></div>
    <div class="fence-band bottom"></div>

    <span class="law law-forest">The Indian Forest Act, 1927</span>
    <span class="law law-rights">The Forest Rights Act, 2006</span>
    <span class="law law-biodiversity">Biological Diversity Act, 2002</span>
    <span class="law law-wildlife">The Wild Life (Protection) Act, 1972</span>
    <span class="law law-conservation">Forest (Conservation) Act, 1980</span>

    <p class="author">Author Name</p>
  </main>
</body>
</html>
```